Business Card for Marco Thieblin Analytics and Marco Thieblin Photography

I want a double sided business card: on one side it should be about "Marco Thieblin Photography" and on the other side about "Marco Thieblin Analytics". You find the logos for these two projects in the attachments. The design of the business card should blend well with the colours and fonts used in the logos and should be quite simple, yet look professional and modern.

In addition to my name, there should be content for a telephone number, e-mail address and website. There should be little icons (for telephone, email and web) before these fields. I do not want a postal mail address field.
Lastly you should indicate that people can contact me in the following languages: Lëtzebuergesch, Deutsch, Français, English, Castellano, Ido
This should be very unobtrusive: either in a small muted font or with little icons (preferably without using flags as flags represent nations, not languages - one possibility would be by using the 2 letter ISO codes).

The design should be delivered in Adobe Illustrator format or something similar that I can edit easily, as it's possible that I will change my e-mail address and domain soon.

I hope this was detailed enough but still leaves you some freedom for designing something nice.

Thank you!
Marco

Industry/Entity Type

Business

Contact Information for Business Card

e-mail address: mtb_@orvenmail.example
website: www.marcothieblin.example (for Marco Thieblin Photography)
website: kelvodata.example/mtb (for Marco Thieblin Analytics - this address is likely to change)
phone: +352 691 987 654 (not my real number - I prefer not to publish it on the web)

Requirements
Nice to have
• A speech bubble followed by the 2-letter language codes (lb, de, fr, en, es, io) or even speech bubble icons for every language would be nice and eliminates the need to put text like 'you can contact me in the following languages'.

```html
<!DOCTYPE html>
<html lang="en">
<head>
<meta charset="utf-8">
<title>Marco Thieblin — Business Card</title>
<link rel="stylesheet" href="https://fonts.googleapis.com/css2?family=Cinzel:wght@400;500&family=Work+Sans:wght@400;500&display=swap">
<style>
  :root {
    --backdrop: #3a3a3c;
    --card-dark: #2a2627;
    --card-light: #ffffff;
    --orange: #ee7f1a;
    --blue: #2a9fd8;
    --green: #2e9e46;
    --ink: #3d3d3d;
    --muted: #6b6b6b;
    --white: #f1f1f1;
  }
  * { box-sizing: border-box; margin: 0; padding: 0; }
  html, body { width: 1200px; height: 810px; overflow: hidden; }
  body {
    background: var(--backdrop);
    display: flex;
    flex-direction: column;
    align-items: center;
    justify-content: center;
    gap: 30px;
    font-family: "Work Sans", sans-serif;
  }
  .card {
    width: 660px;
    height: 370px;
    position: relative;
    box-shadow: 0 10px 28px rgba(0,0,0,.45);
  }

  /* Photography side */
  .card--photography {
    background: var(--card-dark);
    display: flex;
    flex-direction: column;
    align-items: center;
    justify-content: center;
  }
  .brand-mark {
    display: flex;
    align-items: center;
    gap: 14px;
    font-family: "Cinzel", serif;
    font-weight: 400;
    color: var(--orange);
    font-size: 30px;
    letter-spacing: 1px;
  }
  .brand-mark__dot {
    width: 14px; height: 14px; border-radius: 50%;
    background: var(--orange);
    flex: none;
  }
  .website {
    margin-top: 52px;
    font-family: "Cinzel", serif;
    font-size: 14px;
    letter-spacing: 3px;
    color: var(--white);
  }
  .website__domain { color: var(--blue); }

  /* Analytics side */
  .card--analytics { background: var(--card-light); }
  .edge-tab {
    position: absolute;
    left: 0; top: 70px;
    width: 12px; height: 44px;
    background: var(--orange);
    border-radius: 0 8px 8px 0;
  }
  .identity {
    position: absolute;
    left: 50px; top: 58px;
  }
  .identity__name {
    font-family: "Cinzel", serif;
    font-weight: 400;
    font-size: 21px;
    color: var(--orange);
    letter-spacing: .5px;
  }
  .identity__role {
    font-family: "Cinzel", serif;
    font-size: 17px;
    color: var(--muted);
    margin-top: 2px;
  }
  .contacts {
    list-style: none;
    margin-top: 12px;
  }
  .contacts li {
    display: flex;
    align-items: center;
    gap: 14px;
    font-size: 15px;
    color: var(--ink);
    line-height: 24px;
    letter-spacing: .5px;
  }
  .contacts svg { width: 14px; height: 14px; flex: none; }
  .divider {
    position: absolute;
    left: 0; top: 205px;
    width: 385px;
    height: 2px;
    background: var(--orange);
  }
  .card--analytics .brand-mark {
    position: absolute;
    left: 400px; top: 190px;
    font-size: 22px;
  }
  .card--analytics .brand-mark__dot { width: 12px; height: 12px; }
  .languages {
    position: absolute;
    left: 50px; top: 262px;
    font-size: 15px;
    line-height: 21px;
    color: var(--ink);
    letter-spacing: .4px;
  }
  .languages__label { color: var(--orange); }
</style>
</head>
<body>

  <section class="card card--photography" aria-label="Photography side">
    <div class="brand-mark">
      <span class="brand-mark__dot"></span>
      <span>Marco Thieblin Photography</span>
    </div>
    <p class="website">WWW.<span class="website__domain">MARCOTHIEBLIN</span>.EXAMPLE</p>
  </section>

  <section class="card card--analytics" aria-label="Analytics side">
    <span class="edge-tab"></span>
    <div class="identity">
      <h1 class="identity__name">PAUL KESSNER</h1>
      <p class="identity__role">Founder</p>
      <ul class="contacts">
        <li>
          <svg viewBox="0 0 14 14" aria-hidden="true"><rect x="2" y="1.5" width="10" height="11" rx="1.5" fill="none" stroke="var(--green)" stroke-width="1.6"/></svg>
          +352 691 987 654
        </li>
        <li>
          <svg viewBox="0 0 14 14" aria-hidden="true"><rect x="1" y="3" width="12" height="8.5" fill="var(--green)"/><path d="M1 3 L7 8 L13 3" fill="none" stroke="#fff" stroke-width="1.2"/></svg>
          mtb_@orvenmail.example
        </li>
        <li>
          <svg viewBox="0 0 14 14" aria-hidden="true"><g fill="none" stroke="var(--green)" stroke-width="1.3"><circle cx="7" cy="7" r="5.8"/><ellipse cx="7" cy="7" rx="2.6" ry="5.8"/><path d="M1.2 7 H12.8 M2 4 H12 M2 10 H12"/></g></svg>
          kelvodata.example/mtb
        </li>
      </ul>
    </div>

    <span class="divider"></span>

    <div class="brand-mark">
      <span class="brand-mark__dot"></span>
      <span>Marco Thieblin Analytics</span>
    </div>

    <p class="languages">
      <span class="languages__label">You can contact me in:</span><br>
      Lëtzebuergesch, Deutsch,<br>
      Français, English, Castellano
    </p>
  </section>

</body>
</html>
```